Bold Website Design for Fitness Trainer - No Coding

We are in need of a bold and unique website design for a personal fitness training company, www.TessaLorvel.com. We need DESIGN ONLY for three pages. These will be a homepage, a lead capture page, and one internal page with a sidebar. The design will be used for coding a wordpress theme, if that matters for the designer.

Tessa Lorvel Fitness Training
2738 E 19th St #415
Austin, TX 78705
512-607-4918
http://www.tessalorvel.com

Target Market(s)

18-45 year old male and females making 80k+ a year and looking to get stronger and in shape.

Industry/Entity Type

Fitness

Number of Pages Required

3 page

Font styles to use
Sans Serif

Requirements
Must have
• See attached design specs file.
Nice to have
Should not have
• Boxed layout.
• Dark Background.

```html
<!DOCTYPE html>
<html lang="en">
<head>
<meta charset="utf-8">
<title>Tessa Lorvel Fitness Training</title>
<link href="https://fonts.googleapis.com/css2?family=Oswald:wght@400;500;700&family=Open+Sans:wght@400;600;700&family=Montserrat:wght@600;700&display=swap" rel="stylesheet">
<style>
:root{
  --cyan:#1fb4e6;
  --pink:#ec1e8c;
  --yellow:#ffe21a;
  --ink:#1b1b1b;
  --text:#555;
  --footer:#222326;
  --footer-deep:#161719;
  --rule:#ec1e8c;
  --social-a:#3b5998;
  --social-b:#d34836;
  --social-c:#3f729b;
  --social-d:#cc181e;
}
*{box-sizing:border-box;margin:0;padding:0}
html,body{width:1200px;height:3333px;overflow:hidden}
body{position:relative;background:#fff;font-family:"Open Sans",Arial,sans-serif;color:var(--text)}
.abs{position:absolute}

/* top bar */
.topbar{left:0;top:0;width:1200px;height:50px;background:#1a1a1a}
.tab{top:0;height:50px;display:flex;align-items:center;gap:14px;padding:0 34px 0 26px;font:700 17px "Open Sans",sans-serif;color:#fff;clip-path:polygon(0 0,100% 0,calc(100% - 22px) 100%,0 100%);white-space:nowrap}
.tab .ico{width:30px;height:30px;border-radius:50%;background:rgba(0,0,0,.35);display:flex;align-items:center;justify-content:center}
.tab-phone{left:0;width:345px;background:var(--cyan)}
.tab-loc{left:322px;width:290px;background:var(--pink);padding-left:46px}
.tab-cal{left:590px;width:280px;background:var(--yellow);color:#222;padding-left:46px}
.top-social{right:40px;top:14px;display:flex;gap:18px}
.top-social span{width:22px;height:22px;background:#ddd;border-radius:3px}

/* header */
.header{left:0;top:50px;width:1200px;height:195px;background:radial-gradient(ellipse at center,#fbf8f1 0%,#efe7d6 70%,#e4d9c3 100%)}
.brand{left:405px;top:95px;display:flex;align-items:center;gap:18px}
.brand .mark{width:110px;height:110px;border-radius:50%;background:var(--yellow)}
.brand .name{font:700 50px "Oswald",sans-serif;color:var(--ink);letter-spacing:1px}

/* nav */
.nav{left:0;top:245px;width:1200px;height:25px;background:var(--yellow)}
.nav ul{list-style:none;display:flex;margin-left:72px;height:25px}
.nav li{font:500 16px "Oswald",sans-serif;color:#222;padding:0 16px;line-height:25px}
.nav li.active{background:var(--pink);color:#fff}
.free{left:940px;top:212px;width:185px;height:52px;background:var(--pink);color:#fff;font:500 20px "Oswald",sans-serif;display:flex;align-items:center;justify-content:center;border:2px solid #fff}

/* hero */
.hero{left:0;top:270px;width:1200px;height:328px;background:linear-gradient(90deg,#0b0b0b 0%,#1e1e1e 40%,#4a4a4a 70%,#151515 100%)}
.hero-title{left:72px;top:370px;font:500 42px "Oswald",sans-serif;color:var(--cyan)}
.hero-sub{left:72px;top:425px;font:400 30px "Oswald",sans-serif;color:#fff}
.hero-tag{left:72px;top:470px;font:400 19px "Open Sans",sans-serif;color:#ddd}

/* programs */
.section-title{font:500 34px "Oswald",sans-serif;color:var(--ink)}
.program{left:72px;width:695px;height:228px;border-bottom:3px solid var(--rule)}
.program .photo{position:absolute;left:0;top:0;width:333px;height:200px}
.program .body{position:absolute;left:358px;top:0;width:337px}
.program h3{font:700 24px/30px "Montserrat",sans-serif;color:var(--cyan);margin-bottom:10px}
.program p{font:400 13px/24px "Open Sans",sans-serif;color:#555}
.program .more{margin-top:12px;font:600 12px "Open Sans",sans-serif;color:#333}
.program .more b{color:var(--cyan)}

/* sidebar */
.side-title{font:500 22px "Oswald",sans-serif;color:var(--ink)}
.post{left:795px;width:333px;height:250px}
.post .photo{position:absolute;left:0;top:0;width:333px;height:183px;border-bottom:5px solid var(--pink)}
.post .date{position:absolute;left:0;top:120px;width:62px;height:68px;background:var(--pink);color:#fff;text-align:center;font:500 19px/1 "Oswald",sans-serif;padding-top:8px}
.post .date b{display:block;font-size:28px;font-weight:700}
.post .by{position:absolute;left:0;top:193px;font:700 13px "Open Sans",sans-serif;color:#222}
.post .by span{color:var(--pink)}
.post h4{position:absolute;left:0;top:212px;width:333px;font:700 17px/21px "Montserrat",sans-serif;color:var(--cyan)}

.fbbox{left:795px;top:1547px;width:333px;height:375px;border:1px solid #cfd6e4;background:#fff}
.fbbox .bar{height:38px;background:var(--social-a);color:#fff;font:600 20px "Oswald",sans-serif;display:flex;align-items:center;gap:10px;padding-left:10px}
.fbbox .bar i{width:22px;height:22px;background:#fff;border-radius:3px}
.fbbox .feed{margin:12px;height:170px;border:1px solid #ddd;padding:10px;font:400 12px/18px "Open Sans",sans-serif;color:#333}
.fbbox .feed b{color:var(--social-a)}
.fbbox .faces{margin:0 12px;display:grid;grid-template-columns:repeat(6,1fr);gap:4px}
.fbbox .faces span{height:48px;background:linear-gradient(135deg,#8a8a8a,#4b4b4b)}
.fbbox .note{margin:8px 12px;font:400 11px "Open Sans",sans-serif;color:#888}

.grid{left:795px;top:1995px;width:333px;height:333px;display:grid;grid-template-columns:repeat(3,1fr);gap:3px;background:#fff}
.grid span{background:linear-gradient(160deg,#9b9b9b,#3a3a3a)}
.follow{left:795px;top:2350px;width:238px;height:40px;background:#111;color:#fff;font:600 15px "Open Sans",sans-serif;display:flex;align-items:center;justify-content:center;border-radius:2px}

/* call to action */
.cta{left:0;top:2464px;width:1200px;height:486px;background:linear-gradient(180deg,#0d3a52 0%,#126a8e 45%,#0a2f44 100%)}
.cta-circle{left:183px;top:2700px;width:145px;height:145px;border-radius:50%;background:var(--cyan);border:5px solid #fff;color:#fff;font:700 34px/36px "Oswald",sans-serif;text-align:center;padding-top:30px;z-index:2}
.cta-box{left:297px;top:2722px;width:614px;height:100px;background:rgba(0,0,0,.35);border:4px solid var(--yellow);display:flex;align-items:center;padding-left:48px;font:700 66px "Oswald",sans-serif;color:var(--yellow);letter-spacing:1px}
.cta-btn{left:540px;top:2810px;width:126px;height:34px;background:var(--pink);color:#fff;font:700 15px "Open Sans",sans-serif;display:flex;align-items:center;justify-content:center;border-radius:3px;border:2px solid #fff}

/* footer */
.footer{left:0;top:2950px;width:1200px;height:328px;background:var(--footer)}
.foot-mark{left:565px;top:2912px;width:70px;height:70px;border-radius:50%;background:var(--yellow);border:4px solid var(--footer)}
.foot-h{font:600 17px "Oswald",sans-serif;color:#fff;letter-spacing:1px}
.contact{left:72px;width:300px;display:flex;gap:14px;font:400 14px/20px "Open Sans",sans-serif;color:#aaa}
.contact svg{flex:none;margin-top:2px}
.links{left:430px;top:3090px;list-style:none;font:400 14px/31px "Open Sans",sans-serif;color:#aaa}
.links li::before{content:"› ";color:#777}
.social-btn{left:792px;width:212px;height:34px;display:flex;align-items:center;gap:10px;padding-left:8px;font:400 14px "Open Sans",sans-serif;color:#fff;border-radius:2px}
.social-btn i{width:18px;height:18px;background:rgba(255,255,255,.85);border-radius:2px}
.copy{left:0;top:3278px;width:1200px;height:55px;background:var(--footer-deep);font:400 13px "Open Sans",sans-serif;color:#999;display:flex;align-items:center;justify-content:space-between;padding:0 72px}
</style>
</head>
<body>

<!-- top bar -->
<div class="abs topbar"></div>
<div class="abs tab tab-phone"><span class="ico"><svg width="16" height="16" viewBox="0 0 24 24"><path fill="#fff" d="M6.6 10.8a15.1 15.1 0 0 0 6.6 6.6l2.2-2.2c.3-.3.7-.4 1-.2 1.1.4 2.3.6 3.6.6.6 0 1 .4 1 1V20c0 .6-.4 1-1 1C10.6 21 3 13.4 3 4c0-.6.4-1 1-1h3.5c.6 0 1 .4 1 1 0 1.3.2 2.5.6 3.6.1.3 0 .7-.2 1z"/></svg></span>512-607-4918</div>
<div class="abs tab tab-loc"><span class="ico"><svg width="16" height="16" viewBox="0 0 24 24"><path fill="#fff" d="M12 2a7 7 0 0 0-7 7c0 5.2 7 13 7 13s7-7.8 7-13a7 7 0 0 0-7-7zm0 9.5A2.5 2.5 0 1 1 12 6.5a2.5 2.5 0 0 1 0 5z"/></svg></span>Training Locations</div>
<div class="abs tab tab-cal"><span class="ico"><svg width="16" height="16" viewBox="0 0 24 24"><rect x="4" y="5" width="16" height="15" rx="2" fill="none" stroke="#fff" stroke-width="2"/><path d="M4 10h16M8 3v4M16 3v4" stroke="#fff" stroke-width="2"/></svg></span>Training Calendar</div>
<div class="abs top-social"><span></span><span></span><span></span><span></span><span></span></div>

<!-- header -->
<div class="abs header"></div>
<div class="abs brand"><span class="mark"></span><span class="name">Tessa Lorvel</span></div>

<!-- nav -->
<nav class="abs nav"><ul><li>HOME</li><li class="active">PROGRAMS</li><li>MEET YOUR TRAINER</li><li>BLOG</li><li>CONTACT ME</li></ul></nav>
<div class="abs free">FREE SESSION!</div>

<!-- hero -->
<div class="abs hero" role="img" aria-label="Dark gym photo of a woman training"></div>
<div class="abs hero-title">Tessa Lorvel</div>
<div class="abs hero-sub">Personal Trainer and Workouts Custom Tailored to you</div>
<div class="abs hero-tag">Lose Weight Feel Sexy &amp; be Amazing</div>

<!-- programs -->
<h2 class="abs section-title" style="left:72px;top:650px">PROGRAMS</h2>

<div class="abs program" style="top:717px">
  <div class="photo" role="img" aria-label="Woman lifting dumbbells in a gym" style="background:linear-gradient(135deg,#c9a27a,#6b4a35)"></div>
  <div class="body">
    <h3>Programes name here</h3>
    <p>Lorem ipsum dolor sit amet, consectetur adipiscing elit, sed do eiusmod tempor incididunt ut labore et dolore magna aliqua. Ut enim ad minim veniam, quis nostrud exercitation ullamco laboris nisi ut aliquip ex ea commodo consequat.</p>
    <div class="more">READ MORE <b>→</b></div>
  </div>
</div>
<div class="abs program" style="top:972px">
  <div class="photo" role="img" aria-label="Woman training with cable machine" style="background:linear-gradient(135deg,#2a2a2a,#4a7a94)"></div>
  <div class="body">
    <h3>Programes name here</h3>
    <p>Lorem ipsum dolor sit amet, consectetur adipiscing elit, sed do eiusmod tempor incididunt ut labore et dolore magna aliqua. Ut enim ad minim veniam, quis nostrud exercitation ullamco laboris nisi ut aliquip ex ea commodo consequat.</p>
    <div class="more">READ MORE <b>→</b></div>
  </div>
</div>
<div class="abs program" style="top:1228px">
  <div class="photo" role="img" aria-label="Smiling woman in a gym" style="background:linear-gradient(135deg,#a89a8a,#d8c4a6)"></div>
  <div class="body">
    <h3>Programes name here</h3>
    <p>Lorem ipsum dolor sit amet, consectetur adipiscing elit, sed do eiusmod tempor incididunt ut labore et dolore magna aliqua. Ut enim ad minim veniam, quis nostrud exercitation ullamco laboris nisi ut aliquip ex ea commodo consequat.</p>
    <div class="more">READ MORE <b>→</b></div>
  </div>
</div>
<div class="abs program" style="top:1483px">
  <div class="photo" role="img" aria-label="Fit woman standing in a bright gym" style="background:linear-gradient(135deg,#e6e6e6,#7d7d7d)"></div>
  <div class="body">
    <h3>Programes name here</h3>
    <p>Lorem ipsum dolor sit amet, consectetur adipiscing elit, sed do eiusmod tempor incididunt ut labore et dolore magna aliqua. Ut enim ad minim veniam, quis nostrud exercitation ullamco laboris nisi ut aliquip ex ea commodo consequat.</p>
    <div class="more">READ MORE <b>→</b></div>
  </div>
</div>
<div class="abs program" style="top:1739px">
  <div class="photo" role="img" aria-label="Woman doing dumbbell curl on dark background" style="background:linear-gradient(135deg,#1e1e1e,#8a5a44)"></div>
  <div class="body">
    <h3>Programes name here</h3>
    <p>Lorem ipsum dolor sit amet, consectetur adipiscing elit, sed do eiusmod tempor incididunt ut labore et dolore magna aliqua. Ut enim ad minim veniam, quis nostrud exercitation ullamco laboris nisi ut aliquip ex ea commodo consequat.</p>
    <div class="more">READ MORE <b>→</b></div>
  </div>
</div>
<div class="abs program" style="top:1994px">
  <div class="photo" role="img" aria-label="Woman lifting a barbell" style="background:linear-gradient(135deg,#f2f2f2,#9a9a9a)"></div>
  <div class="body">
    <h3>Programes name here</h3>
    <p>Lorem ipsum dolor sit amet, consectetur adipiscing elit, sed do eiusmod tempor incididunt ut labore et dolore magna aliqua. Ut enim ad minim veniam, quis nostrud exercitation ullamco laboris nisi ut aliquip ex ea commodo consequat.</p>
    <div class="more">READ MORE <b>→</b></div>
  </div>
</div>

<!-- sidebar -->
<h3 class="abs side-title" style="left:795px;top:710px">BLOG CATEGORIES</h3>
<div class="abs post" style="top:753px">
  <div class="photo" role="img" aria-label="Arm holding a dumbbell" style="background:linear-gradient(135deg,#1a2c48,#8a5a4a)"></div>
  <div class="date">MAY<b>08</b></div>
  <div class="by">POSTED BY <span>DANA REYES</span></div>
  <h4>Lorem ipsum dolor sit amet dosis orem ipsum reliable</h4>
</div>
<div class="abs post" style="top:1014px">
  <div class="photo" role="img" aria-label="Arm holding a dumbbell" style="background:linear-gradient(135deg,#1a2c48,#8a5a4a)"></div>
  <div class="date">MAY<b>08</b></div>
  <div class="by">POSTED BY <span>DANA REYES</span></div>
  <h4>Lorem ipsum dolor sit amet dosis orem ipsum reliable</h4>
</div>
<div class="abs post" style="top:1275px">
  <div class="photo" role="img" aria-label="Arm holding a dumbbell" style="background:linear-gradient(135deg,#1a2c48,#8a5a4a)"></div>
  <div class="date">MAY<b>08</b></div>
  <div class="by">POSTED BY <span>DANA REYES</span></div>
  <h4>Lorem ipsum dolor sit amet dosis orem ipsum reliable</h4>
</div>

<div class="abs fbbox">
  <div class="bar"><i></i>Like Me on Socialbook</div>
  <div class="feed"><b>Tessa Lorvel</b><br>Yesterday at 9:15am<br><br>#trainingout and getting #stronger in the process! #Teamwork #inspiration #Fitgirl #fitness #letsgo #dedicated</div>
  <div class="faces"><span></span><span></span><span></span><span></span><span></span><span></span><span></span><span></span><span></span><span></span><span></span><span></span></div>
  <div class="note">Socialbook social plugin</div>
</div>

<h3 class="abs side-title" style="left:795px;top:1950px">SNAPGRAM</h3>
<div class="abs grid" role="img" aria-label="Grid of black and white fitness photos"><span></span><span></span><span></span><span></span><span></span><span></span><span></span><span></span><span></span></div>
<div class="abs follow">Follow Us On Snapgram</div>

<!-- call to action -->
<div class="abs cta" role="img" aria-label="Blue toned gym scene with weights"></div>
<div class="abs cta-circle">TRY IT<br>FREE</div>
<div class="abs cta-box">GET STARTED TODAY</div>
<div class="abs cta-btn">CLICK HERE</div>

<!-- footer -->
<div class="abs footer"></div>
<div class="abs foot-mark"></div>

<div class="abs foot-h" style="left:72px;top:3030px">CONTACT INFO</div>
<div class="abs contact" style="top:3090px"><svg width="16" height="18" viewBox="0 0 24 24"><path fill="#888" d="M12 2a7 7 0 0 0-7 7c0 5.2 7 13 7 13s7-7.8 7-13a7 7 0 0 0-7-7zm0 9.5A2.5 2.5 0 1 1 12 6.5a2.5 2.5 0 0 1 0 5z"/></svg><span>2738 E 19th St #415,<br>Austin, TX - 78705</span></div>
<div class="abs contact" style="top:3148px"><svg width="16" height="18" viewBox="0 0 24 24"><path fill="#888" d="M6.6 10.8a15.1 15.1 0 0 0 6.6 6.6l2.2-2.2c.3-.3.7-.4 1-.2 1.1.4 2.3.6 3.6.6.6 0 1 .4 1 1V20c0 .6-.4 1-1 1C10.6 21 3 13.4 3 4c0-.6.4-1 1-1h3.5c.6 0 1 .4 1 1 0 1.3.2 2.5.6 3.6.1.3 0 .7-.2 1z"/></svg><span>Phone: 512-607-4918<br>Fax: 512-607-4919</span></div>
<div class="abs contact" style="top:3206px"><svg width="16" height="18" viewBox="0 0 24 24"><rect x="2" y="5" width="20" height="14" rx="2" fill="#888"/><path d="M3 6l9 7 9-7" stroke="#222" stroke-width="2" fill="none"/></svg><span>Email: info@tessalorvel.com<br>Website: www.TessaLorvel.com</span></div>

<div class="abs foot-h" style="left:430px;top:3030px">RESOURCES</div>
<ul class="abs links"><li>Resources link 1</li><li>Resources link 2</li><li>Resources link 3</li><li>Resources link 4</li><li>Resources link 5</li></ul>

<div class="abs foot-h" style="left:792px;top:3030px">SOCIAL MEDIA</div>
<div class="abs social-btn" style="top:3090px;background:var(--social-a)"><i></i>Follow Us On Socialbook</div>
<div class="abs social-btn" style="top:3131px;background:var(--social-b)"><i></i>Follow Us On Circles+</div>
<div class="abs social-btn" style="top:3172px;background:var(--social-c)"><i></i>Follow Us On Snapgram</div>
<div class="abs social-btn" style="top:3213px;background:var(--social-d)"><i></i>Follow Us On Vidtube</div>

<div class="abs copy"><span>© 2015 TessaLorvel. All Rights Reserved &nbsp;|&nbsp; Phone: 512-607-4918</span><span>Privacy Policy &nbsp;|&nbsp; Terms of Use</span></div>

</body>
</html>
```